1. Overview of company:
Copper Fern Mobile solutions private Ltd is one of the leading innovators & providers of Value added services (VAS) and telecom solutions to the top telecom operators across the world. We are the pioneer of several telecom technologies and products with our solutions empowering over 40 telecom giant in 51 countries.

2. Product Overview:
Vocal Twist is the most innovative voice morphing mobile app that has revolutionized the concept of IVR based offerings for telecom operators across the world. It lets you talk to your friend in a voice of your choice at just the press of a button. In addition to every call, users can now speak to their friends with background sounds of their choice.

In simple words: If person A calls person B, person A can choose the voice he wants B to listen, Words and sentences remain same just the voice changes. Person A can even activate a background sound for both of them while talking.

3. Objective of the design:
The purpose of this campaign is to establish Vocal Twist as Innovative, Lively, Youthful, Fun mobile app generally used for spreading smiles via pranks. The primary objective is to persuade the audience to download and use Vocal Twist mobile app, as well as to spread and characterize this new app.

4. Product layout:
Page 1: Landing Page
- pictorial explanation, what Vocal Twist stands for

Page 2: Home Screen options
-Navigation to vocal twist
-Navigation to sound scenery

Page 3: Vocal Twist options
-Female
-Cartoon
-King
-Bunny

Page 4: Sound scenery options
-Romantic
-Airport
-Traffic
-Football
-Church
-Beach

5. Target Audience
The users of the mobile app will be teenager whose age ranges from 16-27. The demographics are not restricted to a particular country and will be present on global level.

6. Deliverable
- 4 Uncoded screen and icon for mobile app "Vocal Twist"
- Our company name is "Copper Fern" , we would like to see designs that use Black and Green, at the same time its not mandatory.
-Design should communicate what the app stands for "Changing voice of caller"

Target Market(s)

User of the mobile app will be teenagers whose age ranges from 16-27. The demographics are not restricted to a particular country and will be present on global level. It's for masses.

Industry/Entity Type

Telecommunications

Requirements
Must have
• The design should be self explanatory, what the app stands for.
• Editable format for integration purpose.
Nice to have
• Would prefer Icons and very few words.
• Professional, elegant at the same time trendy designs.

```html
<!DOCTYPE html>
<html lang="en">
<head>
<meta charset="utf-8">
<title>Vocal Twist – Morph Screen</title>
<link rel="stylesheet" href="https://fonts.googleapis.com/css2?family=Oswald:wght@400;500;600&display=swap">
<style>
  :root {
    --stage: #2f3130;
    --screen-bg: #e4e4da;
    --white: #ffffff;
    --green: #8cc63f;
    --green-dark: #6fa52a;
    --accent-ink: #2b3a12;
    --ink: #5a5a55;
    --ink-soft: #9a9a92;
    --tile-border: #c9c9be;
  }
  * { box-sizing: border-box; margin: 0; padding: 0; }
  html, body { width: 1200px; height: 801px; overflow: hidden; }
  body {
    background: var(--stage);
    font-family: "Oswald", sans-serif;
    display: flex; align-items: center; justify-content: center;
  }
  .app-screen {
    width: 380px; height: 676px;
    background: var(--screen-bg);
    display: flex; flex-direction: column;
  }
  .app-header {
    height: 64px; background: var(--white);
    display: flex; align-items: center; justify-content: center; gap: 8px;
    border-bottom: 1px solid var(--tile-border);
  }
  .brand-mark { width: 18px; height: 18px; background: var(--green); }
  .brand-name { font-size: 17px; font-weight: 500; color: var(--ink); letter-spacing: .5px; }
  .app-body { flex: 1; padding: 16px 22px 0; }
  .section-bar {
    background: var(--green); color: var(--white);
    height: 36px; display: flex; align-items: center; justify-content: center;
    font-size: 19px; font-weight: 600; letter-spacing: .8px; text-transform: uppercase;
  }
  .section-bar .accent { color: var(--accent-ink); margin-left: 6px; }
  .tile-row { display: flex; flex-wrap: wrap; gap: 10px; padding: 14px 8px; }
  .tile {
    width: 44px; height: 44px; background: var(--white);
    border: 1px solid var(--tile-border);
    display: flex; align-items: center; justify-content: center;
    color: var(--ink);
  }
  .tile svg { width: 26px; height: 26px; fill: none; stroke: currentColor; stroke-width: 1.8; stroke-linecap: round; stroke-linejoin: round; }
  .tile.is-active { background: var(--green); border-color: var(--green-dark); color: var(--white); }
  .tile.more { font-size: 12px; font-weight: 500; letter-spacing: .5px; }
  .slider {
    background: var(--white); border: 1px solid var(--tile-border); border-radius: 4px;
    margin: 0 8px 16px; padding: 6px 14px 8px;
  }
  .slider-label { text-align: center; font-size: 11px; letter-spacing: .8px; color: var(--ink-soft); text-transform: uppercase; }
  .slider-label strong { color: var(--green-dark); font-weight: 600; }
  .slider-track { display: flex; align-items: center; gap: 10px; color: var(--ink); font-size: 16px; margin-top: 2px; }
  .track { flex: 1; height: 4px; background: var(--tile-border); border-radius: 2px; position: relative; }
  .track-fill { position: absolute; left: 0; top: 0; bottom: 0; background: var(--green); border-radius: 2px; }
  .player { padding: 0 8px; }
  .player-status { font-size: 11px; letter-spacing: .8px; color: var(--ink-soft); text-transform: uppercase; display: flex; justify-content: space-between; padding: 0 0 0 44px; }
  .player-row { display: flex; align-items: center; gap: 14px; margin-top: 4px; }
  .record-dot { width: 18px; height: 18px; border-radius: 50%; background: var(--ink); }
  .player-bar {
    flex: 1; height: 30px; background: var(--white); border: 1px solid var(--tile-border); border-radius: 4px;
    display: flex; align-items: center; gap: 10px; padding: 0 12px;
  }
  .play-icon { width: 0; height: 0; border-left: 9px solid var(--ink); border-top: 6px solid transparent; border-bottom: 6px solid transparent; }
  .app-nav { height: 62px; background: var(--green); display: flex; margin-top: 18px; }
  .nav-item {
    flex: 1; display: flex; flex-direction: column; align-items: center; justify-content: center; gap: 3px;
    color: var(--white); font-size: 9px; letter-spacing: .8px; text-transform: uppercase; font-weight: 500;
  }
  .nav-item svg { width: 24px; height: 24px; fill: none; stroke: currentColor; stroke-width: 1.8; stroke-linecap: round; stroke-linejoin: round; }
  .nav-item.is-active { background: var(--white); color: var(--green-dark); }
</style>
</head>
<body>
<main class="app-screen">
  <header class="app-header">
    <span class="brand-mark"></span>
    <span class="brand-name">Copper Fern</span>
  </header>

  <section class="app-body">
    <h2 class="section-bar">Choose your<span class="accent">Voice</span></h2>
    <div class="tile-row">
      <div class="tile" title="Female"><svg viewBox="0 0 24 24"><path d="M2 12c3-5 6-5 10-3 4-2 7-2 10 3-3 5-7 6-10 6s-7-1-10-6z"/><path d="M2 12h20"/></svg></div>
      <div class="tile" title="Cartoon"><svg viewBox="0 0 24 24"><circle cx="12" cy="12" r="9"/><circle cx="9" cy="10" r="1"/><circle cx="15" cy="10" r="1"/><path d="M8 14c2 3 6 3 8 0"/></svg></div>
      <div class="tile is-active" title="King"><svg viewBox="0 0 24 24"><path d="M4 19h16l1-11-5 4-4-6-4 6-5-4z"/></svg></div>
      <div class="tile" title="Bunny"><svg viewBox="0 0 24 24"><path d="M9 11V3c-2 0-2 6-1 8M15 11V3c2 0 2 6 1 8"/><circle cx="12" cy="16" r="5"/></svg></div>
      <div class="tile more">MORE</div>
    </div>
    <div class="slider">
      <p class="slider-label"><strong>King</strong> Voice distortion level</p>
      <div class="slider-track"><span>–</span><div class="track"><div class="track-fill" style="width:45%"></div></div><span>+</span></div>
    </div>

    <h2 class="section-bar">Select an<span class="accent">Ambiance</span></h2>
    <div class="tile-row">
      <div class="tile" title="Romantic"><svg viewBox="0 0 24 24"><path d="M12 20s-8-5-8-11a4 4 0 0 1 8-1 4 4 0 0 1 8 1c0 6-8 11-8 11z"/></svg></div>
      <div class="tile is-active" title="Airport"><svg viewBox="0 0 24 24"><path d="M12 2v20M4 13l8-4 8 4M8 21l4-2 4 2"/></svg></div>
      <div class="tile" title="Traffic"><svg viewBox="0 0 24 24"><rect x="8" y="2" width="8" height="18" rx="2"/><circle cx="12" cy="6" r="1.5"/><circle cx="12" cy="11" r="1.5"/><circle cx="12" cy="16" r="1.5"/></svg></div>
      <div class="tile" title="Football"><svg viewBox="0 0 24 24"><circle cx="12" cy="12" r="9"/><path d="M12 8l3 2-1 4h-4l-1-4z"/></svg></div>
      <div class="tile" title="Church"><svg viewBox="0 0 24 24"><path d="M12 2v5M10 4h4M5 21V12l7-5 7 5v9zM10 21v-5h4v5"/></svg></div>
      <div class="tile" title="Beach"><svg viewBox="0 0 24 24"><path d="M3 11a9 9 0 0 1 18 0zM12 11l4 10M4 21h16"/></svg></div>
      <div class="tile more">MORE</div>
    </div>
    <div class="slider">
      <p class="slider-label"><strong>Airport</strong> Ambiance vol.</p>
      <div class="slider-track"><span>–</span><div class="track"><div class="track-fill" style="width:35%"></div></div><span>+</span></div>
    </div>

    <div class="player">
      <p class="player-status"><span>Playing...</span><span>0:06</span></p>
      <div class="player-row">
        <span class="record-dot"></span>
        <div class="player-bar"><span class="play-icon"></span><div class="track"><div class="track-fill" style="width:30%"></div></div></div>
      </div>
    </div>
  </section>

  <nav class="app-nav">
    <div class="nav-item"><svg viewBox="0 0 24 24"><path d="M3 11l9-7 9 7M5 10v10h14V10"/></svg>Home</div>
    <div class="nav-item is-active"><svg viewBox="0 0 24 24"><path d="M3 6h4l10 12h4M3 18h4l10-12h4"/></svg>Morph</div>
    <div class="nav-item"><svg viewBox="0 0 24 24"><rect x="9" y="3" width="6" height="11" rx="3"/><path d="M5 11a7 7 0 0 0 14 0M12 18v3"/></svg>Record</div>
    <div class="nav-item"><svg viewBox="0 0 24 24"><path d="M5 3h4l2 5-3 2a11 11 0 0 0 6 6l2-3 5 2v4a2 2 0 0 1-2 2A17 17 0 0 1 3 5a2 2 0 0 1 2-2z"/></svg>Call</div>
    <div class="nav-item"><svg viewBox="0 0 24 24"><circle cx="12" cy="12" r="3"/><path d="M12 2v3M12 19v3M2 12h3M19 12h3M5 5l2 2M17 17l2 2M5 19l2-2M17 7l2-2"/></svg>Settings</div>
  </nav>
</main>
</body>
</html>
```